Plumbing & Heating bussiness card design

i do all plumbing and heating work and need a catchy design. keep it simple but eye catching nothing gimicky
i do 24hr call outs
landlord safety checks
all aspects of plumbing and heating
boiler breakdowns
flue sure reg number 804617
i have put up my old card. not to bothered about the front but i have put up the back for the details. mobile number and office are the same and the email has changed to tolwenpipes@mailvoro.net

Industry/Entity Type

Safety

Contact Information for Business Card

i do 24hr call outs
landlord safety checks
boiler breakdowns

Requirements
Must have
• i do 24hr call outs
• landlord safety checks
• all aspects of plumbing and heating
• boiler breakdowns
• flue sure reg number 804617

```html
<!DOCTYPE html>
<html lang="en">
<head>
<meta charset="utf-8">
<title>A Tolwen Plumbing &amp; Heating – Business Card</title>
<link href="https://fonts.googleapis.com/css2?family=Montserrat:wght@400;500;600;700&display=swap" rel="stylesheet">
<style>
  :root {
    --stage: #e9e6e1;
    --card-dark: #3b3c40;
    --card-dark-edge: #2c2d30;
    --card-light: #ffffff;
    --ink: #3d3e42;
    --ink-soft: #55565b;
    --brand-blue: #2f8fd6;
    --brand-red: #d9323f;
    --divider: #c9cbd0;
    --badge: #f4d81c;
  }
  * { box-sizing: border-box; margin: 0; padding: 0; }
  html, body {
    width: 1200px; height: 843px; overflow: hidden;
    background: var(--stage);
    font-family: "Montserrat", sans-serif;
  }
  .sheet {
    position: relative; width: 1200px; height: 843px;
    display: flex; align-items: center; justify-content: center; gap: 40px;
  }
  .card {
    position: relative; width: 540px; height: 349px;
    border-radius: 6px; overflow: hidden;
    box-shadow: 0 10px 28px rgba(0,0,0,.22);
  }

  /* Back of card */
  .card--back {
    background: linear-gradient(160deg, var(--card-dark) 0%, var(--card-dark-edge) 100%);
    color: #fff;
    padding: 40px 40px;
  }
  .back__title { font-size: 34px; font-weight: 600; letter-spacing: .5px; line-height: 1; }
  .back__subtitle { font-size: 17px; font-weight: 600; letter-spacing: .6px; margin-top: 4px; }
  .services { list-style: none; margin-top: 14px; }
  .services li {
    position: relative; padding-left: 20px;
    font-size: 15px; font-weight: 400; line-height: 23px;
  }
  .services li::before {
    content: ""; position: absolute; left: 2px; top: 9px;
    width: 7px; height: 7px; border-radius: 50%;
    background: var(--brand-blue);
  }

  /* Front of card */
  .card--front { background: var(--card-light); color: var(--ink); }
  .brand {
    position: absolute; left: 30px; top: 110px; width: 220px;
    display: flex; align-items: flex-start; gap: 10px;
    color: var(--ink);
    font-weight: 700;
  }
  .brand__mark { width: 14px; height: 14px; background: var(--brand-red); margin-top: 8px; flex: none; }
  .brand__name { font-size: 30px; line-height: 1; letter-spacing: .3px; }
  .brand__name span { display: block; font-size: 16px; margin-top: 6px; letter-spacing: .4px; }
  .divider {
    position: absolute; left: 272px; top: 82px; width: 1px; height: 150px;
    background: var(--divider);
  }
  .contact { position: absolute; left: 292px; top: 86px; }
  .contact__name { font-size: 22px; font-weight: 700; color: var(--brand-blue); letter-spacing: 1px; }
  .contact__address { font-size: 14px; line-height: 19px; color: var(--ink-soft); margin-top: 8px; }
  .contact__lines { list-style: none; margin-top: 12px; }
  .contact__lines li {
    display: flex; align-items: center; gap: 8px;
    font-size: 14.5px; line-height: 21px; color: var(--ink-soft);
  }
  .contact__lines svg { width: 13px; height: 13px; fill: var(--brand-blue); flex: none; }
  .reg {
    position: absolute; right: 20px; top: 36px; width: 90px;
    display: flex; flex-direction: column; align-items: center; gap: 5px;
  }
  .reg__badge { width: 58px; height: 58px; background: var(--badge); }
  .reg__number {
    font-size: 9px; font-weight: 700; letter-spacing: .3px;
    color: var(--ink); text-align: center; line-height: 12px;
  }
  .swoosh { position: absolute; left: 0; bottom: 0; width: 540px; height: 120px; }
</style>
</head>
<body>
<main class="sheet">

  <section class="card card--back" aria-label="Card back">
    <h1 class="back__title">A TOLWEN</h1>
    <p class="back__subtitle">PLUMBING &amp; HEATING</p>
    <ul class="services">
      <li>All aspects of Plumbing &amp; Heating</li>
      <li>I do 24hr call outs</li>
      <li>Landlord safety checks</li>
      <li>Heating Installation</li>
      <li>Flue Safety Checks</li>
      <li>General Plumbing</li>
      <li>Bathrooms</li>
      <li>Boiler breakdowns</li>
      <li>Renewables</li>
    </ul>
  </section>

  <section class="card card--front" aria-label="Card front">
    <div class="brand">
      <div class="brand__mark"></div>
      <div class="brand__name">A TOLWEN<span>PLUMBING &amp; HEATING</span></div>
    </div>
    <div class="divider"></div>
    <div class="contact">
      <p class="contact__name">RHYS</p>
      <p class="contact__address">42 Marrowfield Rd<br>Dunhaven, DH4 2LQ</p>
      <ul class="contact__lines">
        <li><svg viewBox="0 0 24 24"><path d="M7 1h10a2 2 0 0 1 2 2v18a2 2 0 0 1-2 2H7a2 2 0 0 1-2-2V3a2 2 0 0 1 2-2zm0 3v14h10V4z"/></svg>07700 900372</li>
        <li><svg viewBox="0 0 24 24"><path d="M2 5h20v14H2zm2 2v.5l8 5 8-5V7zm0 2.8V17h16V9.8l-8 5z"/></svg>tolwenpipes@mailvoro.net</li>
      </ul>
    </div>
    <div class="reg">
      <div class="reg__badge" role="img" aria-label="Flue Sure register badge"></div>
      <p class="reg__number">FLUE SURE<br>REG: 804617</p>
    </div>
    <svg class="swoosh" viewBox="0 0 540 120" preserveAspectRatio="none" aria-hidden="true">
      <path d="M0 28 C 150 60, 330 92, 540 104 L540 120 L0 120 Z" fill="#f1f2f4"/>
      <path d="M0 22 C 150 52, 330 84, 540 96" fill="none" stroke="var(--brand-red)" stroke-width="4"/>
      <path d="M0 32 C 150 64, 330 96, 540 108" fill="none" stroke="var(--brand-blue)" stroke-width="5"/>
    </svg>
  </section>

</main>
</body>
</html>
```